Velvet & Vine by Mona
Text 410.582.3174 to set up and appointment
Instagram is Velvet_VineByMona
Location 4182 Carrow Ln. Ellerton Pa, 21094 Suit 204
Slogan "Polished Looks. Radiant Days.
Specializing in pressicion cuts, blonding, fades, perms, waxing and more

The salon is black, gun metal color mirror with led lights. Green plants and has natural wood countertops for accent colors. Modern yet elegant. I want the card simple but it needs something to really grab the clients attention. I like black, grey, gold, green, natural tones and hints of pink or gold coloring
I’m open to anything. I don’t have a logo. Suggestions are welcome

Target Market(s)

20-60 men and woman

Industry/Entity Type

Hairstylist / barber

The name of the show should be bold. Maybe the letters could raised I also like foil for shine added or a mat finish

Colors

Requirements
Must have
• I also like some floral Floral designs, but not too overpowering. I like Sparkle, Watercolor design, Or a geometric line in the background
Nice to have
• I’m really here because I need creative help. I’m open for suggestions. I’ll post a picture of the salon in inspiration if I can find it.
Should not have
• Checkered background

```html
<!DOCTYPE html>
<html lang="en">
<head>
<meta charset="utf-8">
<title>Velvet &amp; Vine by Mona — Business Card</title>
<link rel="stylesheet" href="https://fonts.googleapis.com/css2?family=Cinzel:wght@500;600&family=Lora:wght@700&family=Montserrat:wght@400;500&display=swap">
<style>
  :root {
    --backdrop: #5d6062;
    --sage: #63a467;
    --sage-light: #b9dc8f;
    --ink: #17221a;
    --charcoal: #232428;
    --gold: #d9a62a;
    --leaf: #5fa35a;
  }
  * { margin: 0; padding: 0; box-sizing: border-box; }
  html, body { width: 1200px; height: 780px; overflow: hidden; }
  body {
    background: var(--backdrop);
    position: relative;
    font-family: "Montserrat", sans-serif;
  }
  .card {
    position: absolute;
    top: 235px;
    width: 540px;
    height: 310px;
    border-radius: 22px;
    overflow: hidden;
  }
  .card--info { left: 40px; background: var(--sage); color: var(--ink); }
  .card--brand { left: 620px; background: var(--charcoal); }

  .floral { position: absolute; }
  .card--info .floral { background: radial-gradient(ellipse at center, rgba(185,220,143,0.45), rgba(185,220,143,0) 70%); }
  .floral--info-bottom { left: 100px; top: 200px; width: 200px; height: 120px; }
  .floral--info-right { left: 430px; top: 50px; width: 120px; height: 160px; }

  .brand-name {
    position: absolute;
    font-family: "Cinzel", serif;
    font-weight: 600;
    line-height: 1.15;
    text-align: right;
  }
  .card--info .brand-name { left: 40px; top: 92px; width: 210px; font-size: 24px; color: var(--ink); }
  .divider {
    position: absolute; left: 268px; top: 40px; width: 1px; height: 135px; background: var(--ink);
  }
  .contacts {
    position: absolute; left: 292px; top: 58px; list-style: none;
    font-size: 11.5px; font-weight: 400; line-height: 1.35;
  }
  .contacts li { display: flex; align-items: flex-start; gap: 9px; margin-bottom: 8px; }
  .contacts svg { flex: none; width: 14px; height: 14px; margin-top: 1px; }
  .plain-mark { flex: none; width: 12px; height: 12px; border: 1.4px solid var(--ink); border-radius: 50%; margin: 2px 1px 0; }
  .slogan {
    position: absolute; left: 30px; top: 168px; width: 230px; text-align: right;
    font-family: "Lora", serif; font-weight: 700; font-size: 12.5px;
  }
  .specialty {
    position: absolute; left: 250px; top: 188px; width: 250px;
    font-size: 10.5px; font-weight: 500; line-height: 1.35; text-align: center;
  }

  .card--brand .floral { background: radial-gradient(ellipse at center, rgba(95,163,90,0.5), rgba(95,163,90,0) 70%); }
  .floral--brand-bottom { left: 50px; top: 130px; width: 260px; height: 190px; }
  .floral--brand-top { left: 400px; top: -20px; width: 160px; height: 140px; }
  .card--brand .brand-name {
    left: 150px; top: 110px; width: 340px; font-size: 36px; color: var(--gold);
  }
</style>
</head>
<body>
  <section class="card card--info" aria-label="Card back with contact details">
    <div class="floral floral--info-right" role="img" aria-label="Light line-drawn flowers and leaves"></div>
    <div class="floral floral--info-bottom" role="img" aria-label="Light line-drawn wildflowers and grasses"></div>
    <h1 class="brand-name">Velvet &amp; Vine<br>by Mona</h1>
    <div class="divider"></div>
    <ul class="contacts">
      <li>
        <svg viewBox="0 0 14 14" fill="none" stroke="currentColor" stroke-width="1.2"><path d="M1.5 2.5h8v5.5h-5l-2.5 2v-2h-.5z"/><path d="M10.5 5h2v5h-.5v2l-2.5-2h-3.5"/></svg>
        <span>410.582.3174</span>
      </li>
      <li>
        <span class="plain-mark"></span>
        <span>Velvet_VineByMona</span>
      </li>
      <li>
        <svg viewBox="0 0 14 14" fill="none" stroke="currentColor" stroke-width="1.2"><path d="M7 13s-4-4.2-4-7.2a4 4 0 0 1 8 0C11 8.8 7 13 7 13z"/><circle cx="7" cy="5.8" r="1.5"/></svg>
        <span>4182 Carrow Ln. Ellerton<br>Pa.21094 Suit 204</span>
      </li>
    </ul>
    <p class="slogan">Polished Looks. Radiant Days.</p>
    <p class="specialty">Specializing in pressicion cuts, blonding, fades, perms, waxing and more</p>
  </section>

  <section class="card card--brand" aria-label="Card front with name">
    <div class="floral floral--brand-top" role="img" aria-label="Green line-drawn flowers and leaves"></div>
    <div class="floral floral--brand-bottom" role="img" aria-label="Green line-drawn wildflowers, allium blooms and grasses"></div>
    <h2 class="brand-name">Velvet &amp; Vine<br>by Mona</h2>
  </section>
</body>
</html>
```